Velmora Conference

We need a pullup banner 23x63 inches. We are attaching an example of a draft that we created. Can you please make it look more professional?
Thank you!

```html
<!DOCTYPE html>
<html lang="en">
<head>
<meta charset="utf-8">
<title>Quillmere Risk – Pull-up Banners</title>
<link href="https://fonts.googleapis.com/css2?family=Anton&family=Poppins:wght@600;700&display=swap" rel="stylesheet">
<style>
  :root {
    --stage: #a9a9a9;
    --white: #ffffff;
    --navy: #14275f;
    --navy-deep: #0d1838;
    --orange: #f0801f;
    --orange-light: #f79a45;
    --coral: #f4775f;
    --sky-top: #2a73dc;
    --sky-bottom: #a9d0f4;
  }
  * { box-sizing: border-box; margin: 0; padding: 0; }
  html, body { width: 1200px; height: 1200px; overflow: hidden; }
  body { background: var(--stage); position: relative; font-family: "Poppins", sans-serif; }

  .banner { position: absolute; top: 0; width: 437px; height: 1200px; overflow: hidden; background: var(--white); }
  .banner--feature { left: 148px; }
  .banner--services { left: 618px; }
  .banner__art { position: absolute; inset: 0; width: 437px; height: 1200px; }

  .brand { position: absolute; display: flex; align-items: center; gap: 12px; }
  .brand__dot { border-radius: 50%; background: var(--orange); flex: none; }
  .brand__name { font-weight: 700; color: var(--navy); letter-spacing: 1px; line-height: 1; white-space: nowrap; }
  .banner--feature .brand { left: 38px; top: 98px; }
  .banner--feature .brand__dot { width: 34px; height: 34px; }
  .banner--feature .brand__name { font-size: 31px; }
  .banner--services .brand { left: 84px; top: 64px; }
  .banner--services .brand__dot { width: 28px; height: 28px; }
  .banner--services .brand__name { font-size: 25px; }

  .headline { position: absolute; font-family: "Anton", sans-serif; font-weight: 400; white-space: nowrap; }
  .headline .accent { color: var(--orange); }
  .headline--light { left: 32px; top: 636px; font-size: 48px; line-height: 58px; color: var(--white); }
  .headline--dark { left: 40px; top: 136px; font-size: 48px; line-height: 53px; color: var(--navy); }

  .service { position: absolute; height: 49px; border: 2px solid var(--orange); border-radius: 9px;
    display: flex; align-items: center; justify-content: center;
    font-family: "Anton", sans-serif; font-size: 32px; color: var(--white); white-space: nowrap; }

  .cta { position: absolute; left: 121px; top: 1018px; width: 195px; height: 41px; border-radius: 13px;
    background: linear-gradient(180deg, var(--orange-light), var(--orange));
    box-shadow: 0 3px 6px rgba(0,0,0,.35);
    display: flex; align-items: center; justify-content: center;
    font-weight: 700; font-size: 20px; letter-spacing: 1px; color: var(--white); }

  .contact { position: absolute; left: 0; top: 1083px; width: 437px; text-align: center;
    font-weight: 600; font-size: 15px; line-height: 22px; letter-spacing: .7px; color: var(--white); }
</style>
</head>
<body>

<section class="banner banner--feature">
  <svg class="banner__art" viewBox="0 0 437 1200">
    <defs>
      <linearGradient id="skyA" x1="0" y1="0" x2="0" y2="1">
        <stop offset="0" stop-color="var(--sky-top)"/>
        <stop offset="1" stop-color="var(--sky-bottom)"/>
      </linearGradient>
      <linearGradient id="navyA" x1="0" y1="0" x2="0" y2="1">
        <stop offset="0" stop-color="var(--navy)"/>
        <stop offset="1" stop-color="var(--navy-deep)"/>
      </linearGradient>
    </defs>
    <rect role="img" aria-label="Photo of wind turbines and solar panels under a blue sky" x="0" y="185" width="437" height="450" fill="url(#skyA)"/>
    <path d="M0,0 L437,0 L437,185 Q218,255 0,195 Z" fill="var(--white)"/>
    <path d="M0,195 Q218,255 437,185 L437,197 Q218,269 0,208 Z" fill="var(--orange)"/>
    <path d="M0,612 Q218,516 437,605 L437,1200 L0,1200 Z" fill="var(--coral)"/>
    <path d="M0,627 Q218,531 437,620 L437,1200 L0,1200 Z" fill="url(#navyA)"/>
  </svg>

  <div class="brand"><span class="brand__dot"></span><span class="brand__name">QUILLMERE RISK</span></div>

  <h1 class="headline headline--light">Scaling <span class="accent">the market</span><br>for <span class="accent">weather</span>,<br><span class="accent">climate</span> and <span class="accent">natural</span><br><span class="accent">catastrophe risk</span><br>transfer.</h1>

  <div class="cta">CONTACT US</div>
  <p class="contact">HELLO@QUILLMERE.EXAMPLE<br>QUILLMERE.EXAMPLE</p>
</section>

<section class="banner banner--services">
  <svg class="banner__art" viewBox="0 0 437 1200">
    <defs>
      <linearGradient id="skyB" x1="0" y1="0" x2="0" y2="1">
        <stop offset="0" stop-color="var(--sky-top)"/>
        <stop offset="1" stop-color="var(--sky-bottom)"/>
      </linearGradient>
      <linearGradient id="navyB" x1="0" y1="0" x2="0" y2="1">
        <stop offset="0" stop-color="var(--navy)"/>
        <stop offset="1" stop-color="var(--navy-deep)"/>
      </linearGradient>
    </defs>
    <rect role="img" aria-label="Photo of wind turbines and solar panels under a blue sky" x="0" y="298" width="437" height="440" fill="url(#skyB)"/>
    <path d="M0,0 L437,0 L437,298 Q218,370 0,305 Z" fill="var(--white)"/>
    <path d="M0,305 Q218,370 437,298 L437,310 Q218,384 0,318 Z" fill="var(--orange)"/>
    <path d="M0,723 Q218,634 437,730 L437,1200 L0,1200 Z" fill="var(--coral)"/>
    <path d="M0,737 Q218,650 437,744 L437,1200 L0,1200 Z" fill="url(#navyB)"/>
  </svg>

  <div class="brand"><span class="brand__dot"></span><span class="brand__name">QUILLMERE RISK</span></div>

  <h2 class="headline headline--dark">Scaling <span class="accent">the market</span><br>for <span class="accent">climate</span> risk<br>transfer</h2>

  <div class="service" style="left:125px; top:753px; width:188px;">Advisory</div>
  <div class="service" style="left:25px; top:821px; width:188px;">Structuring</div>
  <div class="service" style="left:227px; top:823px; width:188px;">Placement</div>
  <div class="service" style="left:23px; top:889px; width:189px;">Underwriting</div>
  <div class="service" style="left:227px; top:889px; width:188px;">Analytics</div>

  <div class="cta">CONTACT US</div>
  <p class="contact">HELLO@QUILLMERE.EXAMPLE<br>QUILLMERE.EXAMPLE</p>
</section>

</body>
</html>
```